Brantley Water Taxi and Transport

Need to redesign our business cards to relay that we do freight logistics and water taxi service. We also work with gov. agencies doing environmental clean up, oil spill response, remote site construction and work with many of the air taxi and helicopter services on Kodiak Island. Out website is www.brantleywatertaxi-example.com to get a better idea of what we do.

Contact Information for Business Card

I have a previous business card but it just has the logo on the front, and a sunset picture on the back with the contact info. It does not relay what we do and what we can help with. I like a simple straight forward design over a busy one.

Colors
3176b5
0455a3
cfdfed

Requirements
Must have
• logo, email, website, phone number

```html
<!DOCTYPE html>
<html lang="en">
<head>
<meta charset="utf-8">
<title>Brantley Water Taxi &amp; Transport – Business Card</title>
<link rel="stylesheet" href="https://fonts.googleapis.com/css2?family=Montserrat:wght@400;500;600;700&display=swap">
<style>
  :root {
    --page-bg: #e9e7e4;
    --card-bg: #f5f6f8;
    --navy: #1f3c88;
    --brand-blue: #3176b5;
    --band-deep: #0f3797;
    --band-light: #2e56b4;
    --accent-orange: #e8912d;
    --text-gray: #6a6a6a;
    --band-text: #e3e9f7;
    --divider: #bfc4cc;
  }
  * { margin: 0; padding: 0; box-sizing: border-box; }
  html, body {
    width: 1200px; height: 1047px; overflow: hidden;
    background: var(--page-bg);
    font-family: "Montserrat", sans-serif;
  }
  .card {
    position: absolute; left: 100px; top: 253px;
    width: 1000px; height: 541px;
    background: var(--card-bg);
    border-radius: 24px;
    overflow: hidden;
    box-shadow: 0 10px 30px rgba(0,0,0,0.12);
  }
  .brand {
    position: absolute; left: 60px; top: 120px; width: 400px;
    text-align: center; color: var(--navy); font-weight: 600;
  }
  .brand-dot {
    width: 96px; height: 96px; border-radius: 50%;
    background: var(--brand-blue); margin: 0 auto 22px;
  }
  .brand-name { font-size: 54px; line-height: 1; letter-spacing: 1px; }
  .brand-sub { font-size: 24px; margin-top: 6px; }
  .divider {
    position: absolute; left: 505px; top: 97px;
    width: 1px; height: 273px; background: var(--divider);
  }
  .contact { position: absolute; left: 547px; top: 92px; width: 430px; }
  .person-name { font-size: 32px; font-weight: 700; color: var(--navy); letter-spacing: 0.5px; line-height: 1.1; }
  .person-role { font-size: 21px; color: var(--accent-orange); margin-top: 2px; }
  .address { margin-top: 30px; font-size: 21px; color: var(--text-gray); line-height: 36px; }
  .lines { margin-top: 18px; font-size: 20px; color: var(--text-gray); line-height: 32px; white-space: nowrap; }
  .lines b { color: var(--accent-orange); font-weight: 600; }
  .lines .web-name { color: var(--navy); }
  .service-band {
    position: absolute; left: 0; bottom: 0; width: 100%; height: 116px;
    background: linear-gradient(90deg, var(--band-deep), var(--band-light) 50%, var(--band-deep));
    display: flex; flex-direction: column; align-items: center; justify-content: center; gap: 12px;
  }
  .service-row { display: flex; gap: 38px; }
  .service { font-size: 22px; color: var(--band-text); display: flex; align-items: center; }
  .service::before {
    content: ""; width: 12px; height: 12px; border-radius: 50%;
    background: var(--accent-orange); margin-right: 9px;
  }
</style>
</head>
<body>
  <div class="card">
    <div class="brand">
      <div class="brand-dot"></div>
      <div class="brand-name">BRANTLEY</div>
      <div class="brand-sub">Water Taxi &amp; Transport</div>
    </div>
    <div class="divider"></div>
    <div class="contact">
      <div class="person-name">DANIEL HARTLEY</div>
      <div class="person-role">Owner</div>
      <div class="address">2417 Harbor View Dr., Suite 210<br>Alaska, Larkspur Island</div>
      <div class="lines">
        <div><b>P</b>: 907-555-0142</div>
        <div><b>E</b>: brantleywatertaxi@example.com</div>
        <div><b>w</b>: www.<span class="web-name">brantleywatertaxi-example</span>.com</div>
      </div>
    </div>
    <div class="service-band">
      <div class="service-row">
        <span class="service">environmental clean up</span>
        <span class="service">remote site construction</span>
        <span class="service">eco tourism</span>
      </div>
      <div class="service-row">
        <span class="service">oil spill response</span>
        <span class="service">much more</span>
      </div>
    </div>
  </div>
</body>
</html>
```